Beauty Salon Industry - Web Design Project

zQuarta is a well-funded start up developing an Online Marketing Platform for small businesses in Europe.
We require a large number of high quality business web designs for our business website builder. Our business websites are seamlessly integrated into our Online Marketing systems and therefore it is important for designers to comply with our Design Guidelines.
This is our second contest and it will focus on the beauty salon industry. We will be running contents every 2-3 weeks for a new industry. Last month, we ran a contest for Builder website designs with 3 top prizes (plus £10 per variation) and we also paid out £25 per design for 20+ entries from designers who did not win the top prizes. So we encourage all entries!
We have included a wire frame this time to encourage you to be as creative as possible with your designs and layout while respecting the following guidelines:
1) You CAN change the layout as much as you like. If you think a vertical menu would look better, then use it. If you think the design would benefit from moving an element to a different location, then you can do that too.
2) You must include ALL the elements in the wire frame in your design.(e.g. latest 2 news entries, a testimonial, 1 gallery image, carousel etc...). Please make sure you have looked through the wire frame and know what is required. Entries that do not include all the elements will not qualify to win.
3) So remember, you CAN change the layout as much as you like but DO NOT remove any elements nor move them to a different page.
4) You may change the size and style of the carousel image. We would like to see as many variations of this as possible.
We are rewarding 3 prizes, and would like the winning designer to design the internal pages to the new design.
As always, if we think your designs could be incorporated into our system, but you do not win the competition, we will reward £25. Therefore, we encourage designers to submit as many designs as possible as we may award up to 25 designs.
Judging criteria : -
1) Visual Design
2) Layout must adhere to best practices and wireframe. If you decide to move elements around significantly please provide reason
3) Functional, informative and drives calls to action
Updates
As usual:
1st place = £350
2nd place = £250
3rd place = £150
Good luck!
Very happy with all the designs submitted so far, and will provide feedback ASAP.
We would like to see you try arranging the elements differently. So please try different navigation types and layouts.
Thanks
Morris
Prize funds for 1st place has been slightly increased.
Thanks
Morris
We have already had some amazing designs submitted. Thanks.
Remember to play with the layout of the elements and try designs with a carousel/slider that is in portrait not just in landscape.
Thanks everyone!
Morris
Hi everyone, we are really enjoying looking through the designs.
We have one NEW requirement. If you have used an image from http://www.frelik-example.com/ in your design, could you please replace it with another.
We are not associated with them.
Thank you.
I have just sent a poll around the office to vote on all the designs and hope to have the results soon.
Good luck and I hope to see all your great designs for our next project in a couple of weeks.
Morris
Hi everyone, we hope you have had a good holiday season. We will be rewarding the prizes very soon, hopefully today or tomorrow.
Thanks
Morris
We are currently going through all the designs that did not win our competition and will be contacting the designers of the designs we would like to use in our system, so please keep an eye on your inbox over the next few days.
Thank you
Morris
Target Market(s)
Beauty Salon Industry
Industry/Entity Type
Beauty Salon
Look and feel
Each slider illustrates characteristics of the customer's brand and the style your logo design should communicate.

```html
<!DOCTYPE html>
<html lang="en">
<head>
<meta charset="utf-8">
<title>Swirl Loft – Hair and Urban Spa</title>
<link rel="stylesheet" href="https://fonts.googleapis.com/css2?family=Arimo:wght@400;700&family=Great+Vibes&family=Libre+Baskerville:ital@0;1&family=Oswald:wght@600&display=swap">
<style>
:root{
  --plum-deep:#5c0a42;
  --plum:#7a0f57;
  --plum-mid:#8e1466;
  --magenta:#c8168a;
  --accent:#9b1a6c;
  --panel:#f4f4f4;
  --text:#333;
  --muted:#555;
  --rule:#b9b9b9;
}
*{box-sizing:border-box;margin:0;padding:0}
html,body{width:911px;height:1200px;overflow:hidden}
body{
  position:relative;font-family:Arimo,Arial,sans-serif;color:var(--text);
  background:linear-gradient(180deg,#6e0d50 0,#7d1260 100px,#6a0c4c 183px,#9b1a72 184px,#7a1058 232px,#650b48 233px,#5c0a42 100%);
}
.glow{position:absolute;left:0;top:0;width:911px;height:183px;
  background:radial-gradient(ellipse 380px 90px at 560px 60px,rgba(255,255,255,.16),transparent 70%),
             radial-gradient(ellipse 300px 60px at 820px 150px,rgba(255,255,255,.1),transparent 70%)}
.brand{position:absolute;left:124px;top:26px;color:#fff}
.brand-name{font-family:Arimo,Arial,sans-serif;font-weight:700;font-size:38px;letter-spacing:.5px;line-height:1}
.brand-tag{font-size:15px;margin:4px 0 0 28px}
.book{position:absolute;left:676px;top:55px;width:118px;height:48px;background:#fff;border-radius:7px;
  text-align:center;box-shadow:0 1px 3px rgba(0,0,0,.3)}
.book-title{font-family:Oswald,sans-serif;font-weight:600;font-size:16px;color:var(--plum);line-height:1;margin-top:8px;letter-spacing:.5px}
.book-phone{font-size:15px;color:var(--magenta);margin-top:2px}
.panel{position:absolute;left:114px;top:112px;width:684px;height:1032px;background:var(--panel)}
.panel-top{position:absolute;left:114px;top:112px;width:684px;height:48px;background:#fff}
.nav{position:absolute;left:102px;top:160px;width:706px;height:48px;
  background:linear-gradient(180deg,#87115f,#6e0c4f);display:flex;align-items:center}
.nav a{position:absolute;top:0;height:48px;line-height:46px;color:#fff;font-size:11px;text-decoration:none}
.nav .active{left:47px;width:69px;text-align:center;background:linear-gradient(180deg,#e21ba3,#b5137f)}
.hero{position:absolute;left:142px;top:215px;width:624px;height:339px;
  background:linear-gradient(100deg,#c84b99 0,#8c4fae 28%,#1d7b9b 44%,#052431 62%,#02141d 100%)}
.hero-brand{position:absolute;left:305px;top:145px;color:#fff;font-family:"Libre Baskerville",serif;font-size:26px;letter-spacing:1px}
.hero-sub{position:absolute;left:315px;top:183px;color:#ddd;font-family:"Libre Baskerville",serif;font-size:8px;letter-spacing:2px}
.hero-line{position:absolute;left:306px;top:218px;color:#fff;font-family:"Libre Baskerville",serif;font-size:19px;line-height:22px}
.hero-arrows{position:absolute;left:290px;top:309px}
.quote{position:absolute;left:139px;top:570px;width:626px;height:74px;background:var(--plum);border-radius:4px;
  border:1px solid #a44;border-color:#9a2a75;color:#fff;font-family:"Libre Baskerville",serif}
.quote p{position:absolute;left:36px;top:8px;width:570px;font-style:italic;font-size:14px;line-height:18px}
.quote cite{position:absolute;right:33px;top:47px;font-size:9px}
.box{position:absolute;background:#fff;border:1px solid #cfcfcf;border-radius:4px;overflow:hidden}
.box h3{height:26px;line-height:27px;text-align:center;color:#fff;font-weight:400;font-size:13px;
  background:linear-gradient(180deg,#8c1163,#6f0c4f)}
.news-box{left:139px;top:667px;width:149px;height:213px}
.product{position:absolute;left:21px;top:38px;width:104px;height:124px;border:1px solid #ccc;
  background:linear-gradient(180deg,#fff,#f0d4d6)}
.tag{position:absolute;left:5px;top:30px;width:42px;height:42px;border-radius:50%;background:#f08a14;color:#fff;
  font-weight:700;font-size:13px;line-height:42px;text-align:center}
.news-box .caption{position:absolute;left:23px;top:170px;font-size:9px;line-height:11px;color:var(--muted)}
.news-box .cta{position:absolute;left:23px;top:196px;font-size:9px;font-weight:700;color:var(--plum)}
.address-box{left:139px;top:900px;width:149px;height:198px}
.map{position:absolute;left:8px;top:36px;width:131px;height:92px;background:linear-gradient(135deg,#efe9d8,#f5e6b0 60%,#efe4c8)}
.address{position:absolute;left:0;width:100%;top:138px;text-align:center;font-size:9px;line-height:11px;color:var(--accent)}
.pill{position:absolute;height:20px;border-radius:10px;background:linear-gradient(180deg,#fafafa,#dcdcdc);
  font-size:10px;color:#444;line-height:20px;padding:0 12px;box-shadow:0 1px 2px rgba(0,0,0,.2)}
.pill svg{vertical-align:-1px;margin-left:3px}
.intro{position:absolute;left:316px;top:666px;width:280px}
.intro h2{font-weight:400;font-size:15px;color:var(--accent);letter-spacing:-.3px}
.intro p{font-size:8px;line-height:13px;color:var(--text);margin-top:10px;text-align:justify}
.post{position:absolute;left:319px;width:280px;border-top:1px dotted var(--rule)}
.post h4{font-weight:400;font-size:12.5px;color:var(--accent);margin-top:12px}
.meta{font-size:8px;margin-top:9px;color:#444}
.meta span{margin-left:22px;color:var(--accent)}
.post p{font-size:8px;line-height:13px;margin-top:9px}
.post em{font-style:normal;color:var(--accent)}
.portrait{position:absolute;left:626px;top:671px;width:144px;height:150px;
  background:radial-gradient(ellipse at 40% 55%,#b08670 0,#8e7a66 40%,#a69a89 100%)}
.hours{left:623px;top:846px;width:149px;height:154px}
.hours table{margin:12px 0 0 12px;font-size:8.5px;border-collapse:collapse}
.hours td{height:17.2px;letter-spacing:.3px}
.hours td+td{color:var(--accent);padding-left:12px}
.partners{position:absolute;left:318px;top:1066px;width:430px;height:56px}
.partner{position:absolute;top:0;height:54px;display:flex;align-items:center;justify-content:center;font-size:15px;color:#555;font-weight:700}
.partner.dark{background:#444;color:#fff;font-size:12px}
.footer{position:absolute;top:1162px;left:0;width:911px;text-align:center;color:#fff;font-size:8.5px;letter-spacing:.3px}
</style>
</head>
<body>
<div class="glow"></div>

<header>
  <div class="brand">
    <div class="brand-name">Swirl Loft</div>
    <div class="brand-tag">Hair and Urban Spa</div>
  </div>
  <div class="book">
    <div class="book-title">BOOK NOW</div>
    <div class="book-phone">020 7946 0815</div>
  </div>
</header>

<div class="panel"></div>
<div class="panel-top"></div>

<nav class="nav">
  <a class="active" href="#">HOME</a>
  <a style="left:134px" href="#">SERVICES</a>
  <a style="left:221px" href="#">GALLERY</a>
  <a style="left:304px" href="#">TESTIMONIALS</a>
  <a style="left:417px" href="#">NEWS</a>
  <a style="left:487px" href="#">ABOUT US</a>
  <a style="left:579px" href="#">CONTACT US</a>
</nav>

<section class="hero" role="img" aria-label="Carousel photo of a model with dark hair under pink and blue light streaks">
  <div class="hero-brand">SWIRL LOFT</div>
  <div class="hero-sub">HAIR &amp; URBAN SPA</div>
  <div class="hero-line">LET OUR HAIR AND<br>BEAUTY SKILLS<br>SWIRL <i>YOU</i> AWAY…</div>
  <svg class="hero-arrows" width="50" height="20" viewBox="0 0 50 20">
    <circle cx="9" cy="10" r="9" fill="#eee"/><path d="M11 5l-5 5 5 5" stroke="#333" stroke-width="2.4" fill="none"/>
    <circle cx="37" cy="10" r="9" fill="#2c8fd6"/><path d="M35 5l5 5-5 5" stroke="#fff" stroke-width="2.4" fill="none"/>
  </svg>
</section>

<blockquote class="quote">
  <p>“My hairstylist, Marisol, was truly amazing. She listened to exactly what i wanted, but also told me exactly what....”</p>
  <cite>- Tessa Morvane -</cite>
</blockquote>

<aside class="box news-box">
  <h3>News Entry</h3>
  <div class="product" role="img" aria-label="Red haircare bottles gift set"></div>
  <div class="tag">£25</div>
  <div class="caption">Complimentary gift<br>for first-time clients!</div>
  <div class="cta">Book Appointment Now</div>
</aside>

<aside class="box address-box">
  <h3>Swirl Address</h3>
  <div class="map" role="img" aria-label="Street map of the salon area in central London"></div>
  <div class="address">12 Fennick Row - London<br>W1X 9ZZ</div>
  <span class="pill" style="left:29px;top:170px">View map<svg width="10" height="8" viewBox="0 0 10 8"><path d="M0 4h8M5 1l3 3-3 3" stroke="#b01a7c" stroke-width="1.6" fill="none"/></svg></span>
</aside>

<section class="intro">
  <h2>Let our hair and beauty skills swirl you away</h2>
  <p>Swirl Loft is a passionate, creative team, dedicated to delivering a second to none, personal salon experience that will 'swirl' your mind</p>
  <p>Where ultimate hairdressing comes hand-in-hand with style, glamour, fashion, innovation and skill to create an exquisite salon experience in the heart of London.</p>
</section>
<span class="pill" style="left:532px;top:774px">More<svg width="10" height="8" viewBox="0 0 10 8"><path d="M0 4h8M5 1l3 3-3 3" stroke="#b01a7c" stroke-width="1.6" fill="none"/></svg></span>

<article class="post" style="top:808px">
  <h4>Book Now for Christmas</h4>
  <div class="meta">1 Dec, 2011 <span>By. Admin</span></div>
  <p>Our salon is usually very busy for the two weeks before Christmas, so please book early:<br>call <em>020 7946 0815</em>, or contact us.</p>
</article>
<article class="post" style="top:913px">
  <h4>Want to be a hair model?</h4>
  <div class="meta">9 Dec, 2011 <span>By. Admin</span></div>
  <p>We always need models for our portfolio. If you want to become one, please contact us, or call <em>020 7946 0815</em></p>
</article>
<span class="pill" style="left:517px;top:1011px">More news<svg width="10" height="8" viewBox="0 0 10 8"><path d="M0 4h8M5 1l3 3-3 3" stroke="#b01a7c" stroke-width="1.6" fill="none"/></svg></span>

<div class="portrait" role="img" aria-label="Gallery photo of a model with a sculpted floral headpiece"></div>

<aside class="box hours">
  <h3>Bussiness Hour</h3>
  <table>
    <tr><td>Monday</td><td>9 a.m - 5 p.m</td></tr>
    <tr><td>Tuesday</td><td>9 a.m - 5 p.m</td></tr>
    <tr><td>Wednesday</td><td>9 a.m - 5 p.m</td></tr>
    <tr><td>Thursday</td><td>9 a.m - 5 p.m</td></tr>
    <tr><td>Friday</td><td>9 a.m - 5 p.m</td></tr>
    <tr><td>Saturday</td><td>9 a.m - 5 p.m</td></tr>
  </table>
</aside>

<section class="partners" aria-label="Partner brands">
  <div class="partner" style="left:0;width:96px">Lumeria</div>
  <div class="partner dark" style="left:120px;width:72px">Brindle &amp; Co</div>
  <div class="partner dark" style="left:236px;width:82px;top:2px;height:50px">Vantor Pro</div>
  <div class="partner" style="left:352px;width:72px">Orvella</div>
</section>

<footer class="footer">Copyright © 2011 SWIRL LOFT limited. All rights reserved.&nbsp; Managed by zQuarta.com &nbsp; I &nbsp; Admin</footer>
</body>
</html>
```